Redesign of business card for Birchline Mechanical

We are looking for a new design for our business cards for Birchline Mechanical. We are a plumbing & HVAC construction company, operating on the West Coast of Canada and USA. Logo attached.
Industry/Entity Type
Construction - Plumbing & HVAC
Contact Information for Business Card
Name, address, phone numbers, email, website address
Look and feel
Each slider illustrates characteristics of the customer's brand and the style your logo design should communicate.

```html
<!DOCTYPE html>
<html lang="en">
<head>
<meta charset="utf-8">
<title>Birchline Mechanical – Business Cards</title>
<link href="https://fonts.googleapis.com/css2?family=Oswald:wght@500;700&family=Arimo:wght@400&display=swap" rel="stylesheet">
<style>
  :root{
    --stage:#2a2a2a;
    --black-card:#161616;
    --slate-card:#475163;
    --white-card:#ffffff;
    --silver:#d4d4d4;
    --ink-black:#1a1a1a;
    --ink-slate:#3f4a5e;
    --text-grey:#444444;
    --rule:#5b6478;
  }
  html,body{margin:0;padding:0;}
  body{width:823px;height:1200px;overflow:hidden;background:var(--stage);font-family:"Arimo",Arial,sans-serif;}
  .set{position:relative;width:823px;height:600px;}
  .card{position:absolute;width:340px;height:194px;border-radius:14px;box-sizing:border-box;}
  .card--front{left:50px;top:120px;display:flex;align-items:center;justify-content:center;gap:10px;}
  .card--front.black{background:var(--black-card);}
  .card--front.slate{background:var(--slate-card);}
  .card--back{left:433px;top:270px;background:var(--white-card);display:flex;align-items:center;padding:0 18px 0 20px;}
  .brand-mark{width:14px;height:14px;flex:none;}
  .brand-name{font-family:"Oswald",sans-serif;font-weight:500;font-size:19px;letter-spacing:1px;text-transform:uppercase;margin:0;}
  .card--front .brand-name{color:var(--silver);}
  .card--front .brand-mark{background:var(--silver);}
  .back-brand{width:130px;display:flex;align-items:center;gap:6px;}
  .back-brand .brand-name{font-size:13px;line-height:1.1;}
  .divider{width:1px;height:100px;background:var(--rule);margin:0 14px 0 8px;flex:none;}
  .details{flex:1;}
  .person{font-family:"Oswald",sans-serif;font-weight:700;font-size:17px;margin:0;letter-spacing:.5px;line-height:1.1;}
  .role{font-size:8.5px;color:var(--text-grey);margin:1px 0 7px;}
  .contact{list-style:none;margin:0;padding:0;}
  .contact li{display:flex;align-items:flex-start;gap:6px;font-size:7.5px;color:var(--text-grey);line-height:1.35;margin-bottom:1px;}
  .contact svg{width:7px;height:7px;flex:none;margin-top:2px;fill:var(--ink-black);}
  .set--black .brand-name.ink,.set--black .person{color:var(--ink-black);}
  .set--black .back-brand .brand-mark{background:var(--ink-black);}
  .set--slate .brand-name.ink,.set--slate .person{color:var(--ink-slate);}
  .set--slate .back-brand .brand-mark{background:var(--ink-slate);}
  .set--slate .contact svg{fill:var(--ink-slate);}
</style>
</head>
<body>

<section class="set set--black">
  <div class="card card--front black">
    <span class="brand-mark"></span>
    <p class="brand-name">Birchline Mechanical</p>
  </div>
  <div class="card card--back">
    <div class="back-brand">
      <span class="brand-mark"></span>
      <p class="brand-name ink">Birchline Mechanical</p>
    </div>
    <div class="divider"></div>
    <div class="details">
      <p class="person">DANIEL REYES</p>
      <p class="role">Founder &amp; CEO</p>
      <ul class="contact">
        <li><svg viewBox="0 0 10 10"><path d="M5 0a3.5 3.5 0 0 0-3.5 3.5C1.5 6 5 10 5 10s3.5-4 3.5-6.5A3.5 3.5 0 0 0 5 0zm0 5a1.5 1.5 0 1 1 0-3 1.5 1.5 0 0 1 0 3z"/></svg>423 Street Address Here, City<br>State &amp; Country, ZIP Code</li>
        <li><svg viewBox="0 0 10 10"><path d="M2 0l2 2.5-1 1.5a6 6 0 0 0 3 3l1.5-1L10 8l-1.5 2C4 10 0 6 0 1.5z"/></svg>1-123-456-7890</li>
        <li><svg viewBox="0 0 10 10"><path d="M2 0l2 2.5-1 1.5a6 6 0 0 0 3 3l1.5-1L10 8l-1.5 2C4 10 0 6 0 1.5z"/></svg>123-456-7890</li>
        <li><svg viewBox="0 0 10 10"><path d="M2.5 0h5v10h-5zM3.5 1v7h3V1z"/></svg>123-456-7890</li>
        <li><svg viewBox="0 0 10 10"><path d="M0 2h10v6H0zM0 2l5 3.5L10 2"/></svg>info@yourwebsitehere.com</li>
        <li><svg viewBox="0 0 10 10"><circle cx="5" cy="5" r="5"/></svg>yourwebsitehere.com</li>
      </ul>
    </div>
  </div>
</section>

<section class="set set--slate">
  <div class="card card--front slate">
    <span class="brand-mark"></span>
    <p class="brand-name">Birchline Mechanical</p>
  </div>
  <div class="card card--back">
    <div class="back-brand">
      <span class="brand-mark"></span>
      <p class="brand-name ink">Birchline Mechanical</p>
    </div>
    <div class="divider"></div>
    <div class="details">
      <p class="person">DANIEL REYES</p>
      <p class="role">Founder &amp; CEO</p>
      <ul class="contact">
        <li><svg viewBox="0 0 10 10"><path d="M5 0a3.5 3.5 0 0 0-3.5 3.5C1.5 6 5 10 5 10s3.5-4 3.5-6.5A3.5 3.5 0 0 0 5 0zm0 5a1.5 1.5 0 1 1 0-3 1.5 1.5 0 0 1 0 3z"/></svg>423 Street Address Here, City<br>State &amp; Country, ZIP Code</li>
        <li><svg viewBox="0 0 10 10"><path d="M2 0l2 2.5-1 1.5a6 6 0 0 0 3 3l1.5-1L10 8l-1.5 2C4 10 0 6 0 1.5z"/></svg>1-123-456-7890</li>
        <li><svg viewBox="0 0 10 10"><path d="M2 0l2 2.5-1 1.5a6 6 0 0 0 3 3l1.5-1L10 8l-1.5 2C4 10 0 6 0 1.5z"/></svg>123-456-7890</li>
        <li><svg viewBox="0 0 10 10"><path d="M2.5 0h5v10h-5zM3.5 1v7h3V1z"/></svg>123-456-7890</li>
        <li><svg viewBox="0 0 10 10"><path d="M0 2h10v6H0zM0 2l5 3.5L10 2"/></svg>info@yourwebsitehere.com</li>
        <li><svg viewBox="0 0 10 10"><circle cx="5" cy="5" r="5"/></svg>yourwebsitehere.com</li>
      </ul>
    </div>
  </div>
</section>

</body>
</html>
```